IT Consulting Business Card Design

We need a business card on our company name....which is a IT consulting and staffing company. We also train masters graduates in various IT courses. 70% of the time these cards will be handed out to the graduate students at the universities. 30% for our clients and business partners. We are uploading our company logo...would like to see something that matches our logo or blends with it. Please visit www.brivolentaxis.com for more details on logo and colors.

Target Market(s)

70% of the time these cards will be handed out to the graduate students at the universities. 30% for our clients and business partners.

Industry/Entity Type

Business

Contact Information for Business Card

Tomas Verlinde
Vice-President
Brivolen Taxis Inc
3187 Corwick Lane, Suite 412
Cedarwick Falls, NJ 07391
tomas@brivolentaxis.com
Office : 1-855-555-0148 X 312
Cell number : 908-555-0193

Requirements
Nice to have
• may be company logo and name on the back of the card and detials on the other side...just a thought..!!

```html
<!DOCTYPE html>
<html lang="en">
<head>
<meta charset="utf-8">
<title>Brivolen Taxis – Business Card</title>
<link href="https://fonts.googleapis.com/css2?family=Arimo:wght@400;700&family=Open+Sans:wght@400;700&family=Fira+Sans+Condensed:wght@700&display=swap" rel="stylesheet">
<style>
  :root {
    --backdrop: #e6e7e8;
    --brand-red: #e01f26;
    --charcoal: #2b2b2b;
    --charcoal-light: #5a5a5a;
    --stripe-grey: #a9a9a9;
    --ink-white: #ffffff;
  }
  * { margin: 0; padding: 0; box-sizing: border-box; }
  html, body {
    width: 1200px;
    height: 1000px;
    overflow: hidden;
    background: var(--backdrop);
  }
  .canvas {
    position: relative;
    width: 1200px;
    height: 1000px;
  }
  .card {
    position: absolute;
    width: 620px;
    height: 370px;
    overflow: hidden;
    box-shadow: 0 18px 30px rgba(0, 0, 0, 0.18);
  }
  .card-art {
    position: absolute;
    inset: 0;
    width: 100%;
    height: 100%;
  }
  .card--front { left: 130px; top: 100px; }
  .card--back  { left: 500px; top: 530px; }

  .holder {
    position: absolute;
    left: 330px;
    top: 150px;
    width: 230px;
    text-align: center;
    color: var(--ink-white);
    font-family: "Arimo", Arial, sans-serif;
  }
  .holder-name {
    font-weight: 700;
    font-size: 19px;
    letter-spacing: 0.3px;
  }
  .holder-title {
    font-weight: 400;
    font-size: 15px;
    margin-top: 1px;
  }
  .contact {
    position: absolute;
    left: 300px;
    top: 240px;
    color: var(--ink-white);
    font-family: "Open Sans", Arial, sans-serif;
    font-style: normal;
    font-size: 13.5px;
    line-height: 1.22;
    white-space: nowrap;
  }
  .contact-company { font-weight: 700; font-size: 14px; }

  .wordmark {
    position: absolute;
    left: 222px;
    top: 150px;
    color: var(--ink-white);
    font-family: "Fira Sans Condensed", "Arial Narrow", sans-serif;
    font-weight: 700;
    font-size: 54px;
    line-height: 1;
    letter-spacing: 0.5px;
    white-space: nowrap;
  }
</style>
</head>
<body>
<main class="canvas">

  <section class="card card--front" aria-label="Card front with contact details">
    <svg class="card-art" viewBox="0 0 620 370" aria-hidden="true">
      <defs>
        <radialGradient id="front-shade" cx="120" cy="60" r="320" gradientUnits="userSpaceOnUse">
          <stop offset="0" stop-color="var(--charcoal-light)"/>
          <stop offset="1" stop-color="var(--charcoal)"/>
        </radialGradient>
      </defs>
      <rect width="620" height="370" fill="var(--brand-red)"/>
      <path d="M0 0 H244 C301 100 301 260 258 370 H0 Z" fill="var(--stripe-grey)"/>
      <path d="M0 0 H228 C285 100 285 260 242 370 H0 Z" fill="url(#front-shade)"/>
      <circle class="brand-dot" cx="125" cy="180" r="68" fill="var(--brand-red)"/>
    </svg>

    <div class="holder">
      <p class="holder-name">TOMAS VERLINDE</p>
      <p class="holder-title">Vice-President</p>
    </div>

    <address class="contact">
      <p class="contact-company">Brivolen Taxis Inc</p>
      <p>3187 Corwick Lane, Suite 412 Cedarwick Falls,</p>
      <p>NJ 07391</p>
      <p>(O): 1-855-555-0148 x 312 (M): 908-555-0193</p>
      <p>Email: tomas@brivolentaxis.com</p>
      <p>Website: www.brivolentaxis.com</p>
    </address>
  </section>

  <section class="card card--back" aria-label="Card back with company name">
    <svg class="card-art" viewBox="0 0 620 370" aria-hidden="true">
      <defs>
        <radialGradient id="back-shade" cx="300" cy="90" r="380" gradientUnits="userSpaceOnUse">
          <stop offset="0" stop-color="var(--charcoal-light)"/>
          <stop offset="1" stop-color="var(--charcoal)"/>
        </radialGradient>
      </defs>
      <rect width="620" height="370" fill="var(--brand-red)"/>
      <path d="M0 0 Q310 88 620 0 V370 Q310 282 0 370 Z" fill="var(--stripe-grey)"/>
      <path d="M0 12 Q310 100 620 12 V358 Q310 270 0 358 Z" fill="url(#back-shade)"/>
      <circle class="brand-dot" cx="140" cy="182" r="62" fill="var(--brand-red)"/>
    </svg>
    <p class="wordmark">BRIVOLEN TAXIS</p>
  </section>

</main>
</body>
</html>
```